Fun, challenging, and inspirational guide for life change - written by a coach, therapist and founde

I need (1) cover design for a book titled:
"THE HEART'S TOOLKIT FOR WORLD-BENDING IDEAS" - the unexpectedly useful craft of trusting yourself and stepping forward

A 2ND COVER will be need for a companion ebook, titled:
"THE HEART'S FIELD MANUAL FOR THRIVING AND JOY - 4 moves to open up and set free the boundless self by embracing your edges

These books will be used to promote a larger suite of products and services devoted to empowering and inspiring a community of OVERCOMERS.

For reference check out www.lanternmakershall.example

I've included some photos for visual reference points.

DESIGNS CONCEPTS:
CLEAN - A BLEND OF PAST AND PRESENT - MODERN AND THE SACRED) (...The Walcott Almanac meets

Target Market(s)

young and aspiring professionals and seasoned pros looking for life-changes due to feeling unfulfilled in their profession and relationships

Industry/Entity Type

Life Coaching

Font styles to use
Serif
Sans Serif

Requirements
Must have
• CREATIVITY - ORIGINALITY - WICKEDLY CLEAN DESIGN- AND IMPACTFUL TRANSLATION OF BRAND CONCEPT - COLOR AND PUNCH
Nice to have
• I included some photos as reference point - **PLEASE SEE THE PHOTOS FOR THE ROAD-ROVERS DESIGNS** - I really like the feeling they provoke - I want to give the viewer a sense of the journey that can be taken when they dive into these books.
• Basically, riff off the design profiles and colors included in the ROAD-ROVER covers.
• MUSTS INCLUDE -
• -ORIGINALITY
• - IMPACT
• - COLOR
• - ORIGINAL DESIGNS+
• +
Should not have
• STAY AWAY FROM...
• 1 OVERUSED AND TRENDY ICONS
• - ESOTERIC IMAGES
• - FLOWERY SCRIPTS
• - I AM REALLY LOOKING FOR A UPDATE OF THE TYPICAL SELF-HELP BOOK COVERS WHICH RELY TOO MUCH ON FLOWERY AND SACRED IMAGERY
• THANK YOU - feel free to unleash your creativity!

```html
<!DOCTYPE html>
<html lang="en">
<head>
<meta charset="utf-8">
<title>The Heart's Toolkit for World-Bending Ideas</title>
<link rel="stylesheet" href="https://fonts.googleapis.com/css2?family=Cinzel+Decorative:wght@400&family=Cinzel:wght@400;700&display=swap">
<style>
  :root {
    --sky-top: #182a4e;
    --sky-mid: #1d3660;
    --sky-bottom: #2f5a85;
    --ink-light: #ffffff;
    --emblem-glow: rgba(255, 255, 255, 0.55);
    --emblem-edge: rgba(255, 255, 255, 0.08);
  }
  html, body {
    margin: 0;
    padding: 0;
    width: 800px;
    height: 1200px;
    overflow: hidden;
    background: var(--sky-top);
  }
  .cover {
    position: relative;
    width: 800px;
    height: 1200px;
    overflow: hidden;
    background: linear-gradient(180deg, var(--sky-top) 0%, var(--sky-mid) 50%, var(--sky-bottom) 100%);
    color: var(--ink-light);
    text-align: center;
  }
  .title {
    position: absolute;
    left: 0;
    top: 0;
    width: 800px;
    margin: 0;
    font-weight: 400;
    font-family: "Cinzel Decorative", "Cinzel", serif;
  }
  .title span {
    position: absolute;
    left: 0;
    width: 800px;
    line-height: 1;
    white-space: nowrap;
  }
  .title-lead {
    top: 60px;
    font-size: 100px;
  }
  .title-middle {
    top: 180px;
    font-size: 60px;
  }
  .title-tail {
    top: 256px;
    font-size: 42px;
  }
  .subtitle {
    position: absolute;
    left: 0;
    top: 334px;
    width: 800px;
    margin: 0;
    font-family: "Cinzel", serif;
    font-weight: 700;
    font-size: 19px;
    line-height: 35px;
    letter-spacing: 0.05em;
    text-transform: uppercase;
  }
  .emblem {
    position: absolute;
    left: 192px;
    top: 496px;
    width: 416px;
    height: 416px;
    border-radius: 50%;
    background: radial-gradient(circle at 50% 50%, var(--emblem-glow) 0%, rgba(255,255,255,0.28) 45%, var(--emblem-edge) 100%);
  }
  .author {
    position: absolute;
    left: 0;
    top: 1044px;
    width: 800px;
    margin: 0;
    font-family: "Cinzel", serif;
    font-weight: 400;
    font-size: 92px;
    line-height: 1;
    white-space: nowrap;
    text-transform: uppercase;
  }
</style>
</head>
<body>
  <main class="cover">
    <h1 class="title">
      <span class="title-lead">The Heart's</span>
      <span class="title-middle">Toolkit For</span>
      <span class="title-tail">World-Bending Ideas</span>
    </h1>
    <p class="subtitle">11 ideas to open up and set free your<br>drive and direction out in the world</p>
    <div class="emblem" role="img" aria-label="White geometric star emblem inside a double circle"></div>
    <p class="author">Author Name</p>
  </main>
</body>
</html>
```